Kestrel Towbars Square Business Card Design

I would like a 2 x 2 square rounded corner business card.my business manufacture vehicle hitches and uses square tubing with rounded corners and would like to incorporate the border to look like the tubing...
2417 Larkmoor Ave. Fenwick Falls, Ohio 43999
(555) 390-6518
dale@kestreltowbars.com
www.kestreltowbars.com

Target Market(s)

automotive / vehicle hitches

Industry/Entity Type

Automotive

Contact Information for Business Card

I would like a 2 x 2 square rounded corner business card.my business manufacture vehicle hitches and uses square tubing with rounded corners and would like to incorporate the border to look like the tubing... and red, white and blue theme colors

Font styles to use
Sans Serif

Colors

Designer to choose colors to be used in the design.

Requirements
Must have
• Boarder
Nice to have
• red, white, blue theme colors
Should not have
• odd colors

```html
<!DOCTYPE html>
<html lang="en">
<head>
<meta charset="utf-8">
<title>Kestrel Towbars – Square Business Card</title>
<link rel="stylesheet" href="https://fonts.googleapis.com/css2?family=Lato:wght@300;400;700;900&family=Encode+Sans+Condensed:wght@400;700&display=swap">
<style>
  :root {
    --navy: #2b3a78;
    --red: #d0103a;
    --paper: #ffffff;
    --steel-dark: #9ea7b0;
    --steel-mid: #c2c9d0;
    --steel-light: #eef2f6;
  }
  * { box-sizing: border-box; margin: 0; padding: 0; }
  html, body {
    width: 1200px; height: 800px; overflow: hidden;
    background: var(--paper);
  }
  .canvas { position: relative; width: 1200px; height: 800px; }

  .card {
    position: absolute; width: 460px; height: 460px;
    border-radius: 64px;
    background: linear-gradient(125deg, var(--steel-mid) 0%, var(--steel-light) 14%, var(--steel-dark) 30%, var(--steel-mid) 48%, var(--steel-light) 60%, var(--steel-dark) 74%, var(--steel-light) 88%, var(--steel-mid) 100%);
  }
  .card--front { left: 112px; top: 144px; }
  .card--back  { left: 627px; top: 146px; }

  .card__lip {
    position: absolute; inset: 40px;
    border-radius: 42px;
    background: linear-gradient(135deg, #d4dae0 0%, #f4f7fa 40%, #b9c1c9 70%, #e8edf2 100%);
  }
  .card__window {
    position: absolute; inset: 52px;
    border-radius: 30px;
    background: var(--paper);
    box-shadow: inset 16px 16px 18px -4px rgba(0,0,0,.8), inset -3px -3px 6px rgba(0,0,0,.08);
  }

  .brand {
    position: absolute; left: 0; right: 0; top: 170px;
    text-align: center;
    font-family: "Lato", sans-serif; font-weight: 900;
    font-size: 50px; line-height: 52px; color: var(--navy);
  }
  .brand__mark {
    display: block; width: 26px; height: 26px; margin: 0 auto 14px;
    background: var(--red);
  }

  .contact { position: absolute; left: 0; right: 0; top: 0; text-align: center; color: var(--navy); }
  .contact__name {
    position: absolute; left: 0; right: 0; top: 108px;
    font-family: "Lato", sans-serif; font-weight: 900; font-size: 31px; letter-spacing: -0.3px;
  }
  .contact__rule {
    position: absolute; left: 110px; width: 240px; top: 153px; height: 5px;
    background: var(--red); border-radius: 50%;
  }
  .contact__role {
    position: absolute; left: 0; right: 0; top: 161px;
    font-family: "Lato", sans-serif; font-weight: 400; font-size: 31px; letter-spacing: 1px;
  }
  .contact__address {
    position: absolute; left: 0; right: 0; top: 210px;
    font-family: "Encode Sans Condensed", sans-serif; font-weight: 400;
    font-size: 28px; line-height: 32px;
  }
  .contact__web {
    position: absolute; left: 0; right: 0; top: 316px;
    font-family: "Encode Sans Condensed", sans-serif; font-weight: 700;
    font-size: 28px; line-height: 30px;
  }
  .contact__email { color: var(--navy); }
  .contact__url { color: var(--red); }
</style>
</head>
<body>
<main class="canvas">
  <section class="card card--front">
    <div class="card__lip"></div>
    <div class="card__window"></div>
    <div class="brand"><span class="brand__mark"></span>Kestrel<br>Towbars</div>
  </section>

  <section class="card card--back">
    <div class="card__lip"></div>
    <div class="card__window"></div>
    <div class="contact">
      <p class="contact__name">Dale R. Whitcomb</p>
      <div class="contact__rule"></div>
      <p class="contact__role">Owner</p>
      <p class="contact__address">2417 Larkmoor Ave.<br>Fenwick Falls, Ohio 43999<br>(555) 390-6518</p>
      <p class="contact__web"><span class="contact__email">dale@kestreltowbars.com</span><br><span class="contact__url">www.kestreltowbars.com</span></p>
    </div>
  </section>
</main>
</body>
</html>
```